Professional Business Card for Commercial Cleaning Company

We need a business card that represents our commercial janitorial cleaning company and represent several brands for our company so we do not want to highlight the logo too much. We want something that says we are professional.
Notes:No website or address as we have many locations and many websites and companies under our corporate name of "Brightvale Holdings, LLC" . Every time we hand a customer a business card they have contacted us via another brand we own but we don't want to have 21 business cards so we want to not focus on Brightvale Holdings, LLC too much since people will automatically ask "What is Brightvale Holdings, LLC" Example: Noodle Barn and Wrap Lantern restaurants are owned by "Zest! Brands" is the corporation name. Same principle here. Except we do not advertise at this time that all of our brands are connected. Hope this helps.
Target Market(s)
Commercial Cleaning
Industry/Entity Type
Janitorial Service
Contact Information for Business Card
Milo Jarvis
Business Development
555-382-9047
sales@brightvaleholdingsllc.example
Requirements
Must have
- Logo with contact information, need to be able to easily edit contact info for others in my office.
Nice to have
- Professional Image. Like to see a colorful bold look and a more standard business card look.
Should not have
- Any type of cleaning icons, tools, people or water.

```html
<!DOCTYPE html>
<html lang="en">
<head>
<meta charset="utf-8">
<title>Brightvale Holdings business card</title>
<link rel="stylesheet" href="https://fonts.googleapis.com/css2?family=Open+Sans:wght@400;600;700&display=swap">
<style>
  :root {
    --page-bg: #e6e4e0;
    --card-black: #060606;
    --card-sheen: #1e1e1e;
    --brand-blue: #0a4c9c;
    --brand-blue-light: #4a95d2;
    --brand-green: #9fd13f;
    --brand-green-light: #cfe98f;
    --text-white: #f4f4f4;
  }
  * { margin: 0; padding: 0; box-sizing: border-box; }
  html, body {
    width: 1200px; height: 1023px; overflow: hidden;
    background: var(--page-bg);
    font-family: "Open Sans", Arial, sans-serif;
  }
  .business-card {
    position: absolute; left: 100px; top: 226px;
    width: 1000px; height: 572px;
    background: linear-gradient(115deg, var(--card-black) 0%, var(--card-sheen) 45%, var(--card-black) 72%);
    overflow: hidden;
    box-shadow: 0 18px 40px rgba(0,0,0,.35);
  }
  .edge-tile { position: absolute; bottom: 0; width: 84px; height: 64px; }
  .tile-blue { background: var(--brand-blue); }
  .tile-green { background: var(--brand-green); }
  .tile-blue-light { background: var(--brand-blue-light); }
  .tile-green-light { background: var(--brand-green-light); }

  .company-name {
    position: absolute; left: 60px; top: 380px;
    font-weight: 600; font-size: 36px; letter-spacing: .3px;
    color: var(--brand-blue-light);
    white-space: nowrap;
  }
  .contact-block {
    position: absolute; right: 130px; top: 70px;
    text-align: right; color: var(--text-white);
  }
  .person-name { font-weight: 700; font-size: 42px; line-height: 1.1; }
  .person-title { font-size: 26px; color: var(--brand-green); margin-top: 4px; }
  .contact-line {
    position: absolute; right: 130px;
    font-size: 23px; line-height: 64px; color: var(--text-white);
    text-align: right; white-space: nowrap;
  }
  .contact-phone { top: 220px; }
  .contact-email { top: 284px; }
  .icon-box {
    position: absolute; right: 0; width: 76px; height: 64px;
    display: flex; align-items: center; justify-content: center;
  }
  .icon-box svg { width: 28px; height: 28px; }
  .icon-phone { top: 220px; }
  .icon-mail { top: 284px; }
  .icon-accent { top: 348px; }
</style>
</head>
<body>
  <section class="business-card">
    <div class="edge-tile tile-blue" style="left:40px"></div>
    <div class="edge-tile tile-green" style="left:220px"></div>
    <div class="edge-tile tile-blue-light" style="left:400px"></div>
    <div class="edge-tile tile-green-light" style="left:580px"></div>

    <div class="company-name">Brightvale Holdings, LLC</div>

    <div class="contact-block">
      <div class="person-name">Milo Jarvis</div>
      <div class="person-title">Business Development</div>
    </div>

    <div class="contact-line contact-phone">555-382-9047</div>
    <div class="contact-line contact-email">sales@brightvaleholdingsllc.example</div>

    <div class="icon-box icon-phone tile-blue">
      <svg viewBox="0 0 24 24" aria-label="Phone"><rect x="3" y="3" width="18" height="18" rx="2" fill="#fff"/><path d="M8 7c0 5 4 9 9 9l1-2-3-1-1 1c-2-1-3-2-4-4l1-1-1-3z" fill="var(--brand-blue)"/></svg>
    </div>
    <div class="icon-box icon-mail">
      <svg viewBox="0 0 24 24" aria-label="Email"><rect x="3" y="5" width="18" height="14" fill="#fff"/><path d="M3 5l9 8 9-8" fill="none" stroke="#060606" stroke-width="2"/></svg>
    </div>
    <div class="icon-box icon-accent tile-green"></div>
  </section>
</body>
</html>
```